Flyer for corporate discount for dog daycare

I own a dog daycare with a large corporate down the road. I am working with the President of the company to offer their employees a discount for my services, Dog Daycare, Overnight Care, Grooming Salon & Spa and Retail. The design should be professional but also have a soft side as people view their dogs similar to human children.

I attached my logo along with our grooming brochure for reference on colors we've been using.

At a minimum the flyer must contain the following information:
Name: The Wagtail Lodge
web address: www.PawHavenStays.example
phone number: 920-555-0148
Address: 4872 Larchmont Lane
Google Map of our location

Title of flyer/program: Corporate V.I.P. (Very Important Pooch) (Can be creative with how to include this such as, Welcome to our Corporate. . .. etc.)

The program offer is: 5% discount
My services: Dog Daycare, Overnight Care, Grooming Salon & Spa and Retail

Target Market(s)

corporate employees, male and female, age 24+

Industry/Entity Type

Daycare

Requirements
Must have
• Must be easy to read and inviting.
Nice to have
• Nice photo dogs playing or inviting photo of dog.
Should not have
• cartoon feel

```html
<!DOCTYPE html>
<html lang="en">
<head>
<meta charset="utf-8">
<title>The Wagtail Lodge – Corporate V.I.P Program</title>
<link href="https://fonts.googleapis.com/css2?family=Lato:wght@400;700;900&display=swap" rel="stylesheet">
<style>
  :root {
    --page-bg: #d9d9dd;
    --lime: #a9c63b;
    --lime-bright: #b5d334;
    --sky: #aadde4;
    --teal: #12b7cf;
    --teal-dark: #0a7f8c;
    --yellow: #f7ea3a;
    --ink: #222222;
    --brown: #3d3020;
    --white: #ffffff;
  }
  * { box-sizing: border-box; margin: 0; padding: 0; }
  html, body { width: 1200px; height: 1200px; overflow: hidden; }
  body { background: var(--page-bg); font-family: "Lato", Arial, sans-serif; position: relative; }

  .flyer { position: absolute; left: 205px; top: 41px; width: 790px; height: 1118px; background: var(--ink); overflow: hidden; }

  .hero-photo { position: absolute; left: 0; top: 0; width: 790px; height: 500px;
    background: linear-gradient(180deg, #3d4a2a 0%, #5f8a32 35%, #6fa238 65%, #5a8a2c 100%); }

  .brand-tab { position: absolute; left: 32px; top: 0; width: 283px; height: 216px; background: var(--lime);
    border-radius: 0 0 24px 24px; display: flex; flex-direction: column; align-items: center; justify-content: center; gap: 16px; }
  .brand-tab .mark { width: 56px; height: 56px; background: var(--brown); }
  .brand-tab .brand-name { font-weight: 900; font-size: 26px; color: var(--brown); letter-spacing: 0.5px; white-space: nowrap; }

  .headline { position: absolute; left: 50px; top: 258px; color: var(--white); font-weight: 900;
    text-shadow: 0 2px 4px rgba(0,0,0,.45); line-height: 1; }
  .headline .intro { font-size: 29px; display: block; margin-bottom: 14px; }
  .headline .title { font-size: 49px; display: block; margin-bottom: 9px; white-space: nowrap; }

  .offer-badge { position: absolute; left: 459px; top: 290px; width: 300px; height: 140px; }

  .service-card { position: absolute; top: 512px; width: 227px; height: 222px; background: var(--sky); border-radius: 5px;
    text-align: center; padding: 131px 6px 0; }
  .service-card h2 { font-weight: 900; font-size: 23px; color: var(--ink); letter-spacing: .3px; white-space: nowrap; }
  .service-card p { font-size: 10.3px; line-height: 13px; color: #2c3b3e; margin-top: 7px; }
  .service-photo { position: absolute; top: 429px; width: 204px; height: 204px; border-radius: 50%;
    border: 8px solid var(--white); }
  .card-daycare { left: 42px; } .card-overnight { left: 284px; } .card-grooming { left: 523px; }
  .photo-daycare { left: 51px; background: radial-gradient(circle at 50% 60%, #5d8e3a, #4a7a2d); }
  .photo-overnight { left: 294px; background: radial-gradient(circle at 50% 55%, #9b5a33, #e8e6e2 70%); }
  .photo-grooming { left: 536px; background: radial-gradient(circle at 55% 45%, #e0a86a, #f0d6c6 75%); }

  .location-heading { position: absolute; left: 38px; width: 360px; top: 755px; text-align: center;
    color: var(--lime-bright); font-weight: 900; font-size: 24px; }
  .location-map { position: absolute; left: 38px; top: 789px; width: 359px; height: 201px; border-radius: 3px;
    background: linear-gradient(135deg, #ecebe7, #dedcd6); }
  .divider { position: absolute; left: 408px; top: 756px; height: 232px; border-left: 2px dashed #8a8a8a; }

  .contact { position: absolute; left: 437px; top: 778px; width: 345px; }
  .contact .services-label { font-weight: 900; font-size: 20px; color: var(--sky); text-decoration: underline; line-height: 24px; }
  .contact .services-list { font-weight: 700; font-size: 19.5px; color: var(--sky); line-height: 24px; white-space: nowrap; }
  .contact .call { font-weight: 900; font-size: 22px; color: var(--lime-bright); margin-top: 17px; }
  .contact .phone { font-weight: 900; font-size: 17.5px; color: var(--white); margin-top: 8px; white-space: nowrap; }
  .contact .online { display: flex; align-items: center; gap: 14px; margin-top: 12px; }
  .contact .online-lines { font-size: 16px; color: var(--white); line-height: 22px; white-space: nowrap; }

  .footer-stripe { position: absolute; left: 0; top: 1008px; width: 790px; height: 10px; background: var(--lime); }
  .footer { position: absolute; left: 0; top: 1018px; width: 790px; height: 82px; background: var(--white);
    display: flex; align-items: center; padding-left: 62px; gap: 26px; }
  .footer .footer-name { font-weight: 900; font-size: 27px; color: var(--brown); white-space: nowrap; }
  .footer .footer-address { font-weight: 700; font-size: 17px; color: var(--brown); white-space: nowrap; }
</style>
</head>
<body>
<main class="flyer">
  <div class="hero-photo" role="img" aria-label="Golden retriever walking on green grass with a pink ball in its mouth"></div>

  <div class="brand-tab">
    <div class="mark"></div>
    <div class="brand-name">The Wagtail Lodge</div>
  </div>

  <h1 class="headline">
    <span class="intro">WELCOME TO OUR</span>
    <span class="title">CORPORATE V.I.P</span>
    <span class="title">PROGRAM!</span>
  </h1>

  <svg class="offer-badge" viewBox="0 0 300 140" aria-label="5% off, limited time only">
    <polygon points="0,62 24,26 24,72" fill="var(--teal-dark)"/>
    <polygon points="24,0 184,20 184,72 24,72" fill="var(--yellow)"/>
    <text x="47" y="58" font-family="Lato, sans-serif" font-weight="900" font-size="40" fill="var(--lime)">5%</text>
    <text x="132" y="58" font-family="Lato, sans-serif" font-weight="900" font-size="22" fill="var(--lime)">OFF</text>
    <polygon points="0,72 184,72 184,62 284,62 284,114 0,114" fill="var(--teal)"/>
    <polygon points="150,114 224,114 150,134" fill="var(--teal-dark)"/>
    <text x="142" y="99" text-anchor="middle" font-family="Lato, sans-serif" font-weight="400" font-size="24" fill="var(--white)" letter-spacing="1">LIMITED TIME ONLY</text>
  </svg>

  <section class="service-card card-daycare">
    <h2>DAYCARE</h2>
    <p>Daycare is available any day during our regular business hours. We offer half days for up to five hours of play</p>
  </section>
  <section class="service-card card-overnight">
    <h2>OVERNIGHT CARE</h2>
    <p>Leaving your pet overnight should not be a stressful time for either of you. Your pet's stay with us will be safe and enjoyable.</p>
  </section>
  <section class="service-card card-grooming">
    <h2>GROOMING</h2>
    <p>From gentle massages, to deep coat conditioning, or moisturizing paw rubs we have our furry friend's best interests in mind.</p>
  </section>
  <div class="service-photo photo-daycare" role="img" aria-label="Puppy playing with a soccer ball on grass"></div>
  <div class="service-photo photo-overnight" role="img" aria-label="Dog sleeping on a soft white blanket"></div>
  <div class="service-photo photo-grooming" role="img" aria-label="Small long-haired dog being groomed with scissors"></div>

  <h2 class="location-heading">OUR LOCATION</h2>
  <div class="location-map" role="img" aria-label="Street map showing the lodge location"></div>
  <div class="divider"></div>

  <section class="contact">
    <div class="services-label">OUR SERVICES</div>
    <div class="services-list">Dog Daycare, Overnight Care,<br>Grooming Salon &amp; Spa and Retail</div>
    <div class="call">Call for more information</div>
    <div class="phone">Ph: 920-555-0148 , Fax: 920-555-0172</div>
    <div class="online">
      <svg width="40" height="40" viewBox="0 0 40 40" aria-hidden="true">
        <circle cx="20" cy="20" r="17" fill="var(--lime)"/>
        <g fill="none" stroke="var(--ink)" stroke-width="1.6">
          <circle cx="20" cy="20" r="9"/>
          <ellipse cx="20" cy="20" rx="4" ry="9"/>
          <line x1="11" y1="20" x2="29" y2="20"/>
          <line x1="12.5" y1="15.5" x2="27.5" y2="15.5"/>
          <line x1="12.5" y1="24.5" x2="27.5" y2="24.5"/>
        </g>
      </svg>
      <div class="online-lines">info@pawhavenstays.example<br>www.PawHavenStays.example</div>
    </div>
  </section>

  <div class="footer-stripe"></div>
  <footer class="footer">
    <span class="footer-name">THE WAGTAIL LODGE</span>
    <span class="footer-address">4872 Larchmont Lane, Brookfield Falls, WI 54900</span>
  </footer>
</main>
</body>
</html>
```